Cocktail Menu

I need a drink menu that will be prited on a heavy weight card designed. I want it to be something differtent that guests will look at then order a drink. The card will be on the bar or given to customers at tables. This is for a upscale restaurant in Northern Virginia. The website is www.HollowmereRestaruant.com if you want to see pictures. I will attach rthe drinks and our logo. I need something really attractive and different. It can be larger then a postcard but not stanadard paper sizes.
Updates

The menu can be larger then a postcard and the front and back can be used if needed.

Industry/Entity Type

Restaurant

```html
<!DOCTYPE html>
<html lang="en">
<head>
<meta charset="utf-8">
<title>Hollowmere Restaurant – Cocktail Menu</title>
<link rel="stylesheet" href="https://fonts.googleapis.com/css2?family=Oswald:wght@400;500&family=Crimson+Text:ital@1&family=Orbitron:wght@500&family=Michroma&display=swap">
<style>
  :root{
    --stage:#584866;
    --panel:#8c3b9e;
    --strip:#f6dbe8;
    --teal:#2aa6c4;
    --heading:#f2e44a;
    --price:#6a1a92;
    --ink:#1c1420;
    --white:#ffffff;
  }
  *{margin:0;padding:0;box-sizing:border-box}
  html,body{width:1200px;height:1000px;overflow:hidden}
  body{background:var(--stage);position:relative;font-family:"Oswald",sans-serif}

  /* ---------- Front: drink list ---------- */
  .menu-card{position:absolute;left:70px;top:70px;width:568px;height:730px;background:var(--strip);overflow:hidden;box-shadow:0 8px 24px rgba(0,0,0,.35)}
  .menu-card .side-glow{position:absolute;inset:0;background:
      radial-gradient(circle at 4% 30%,#ffffff 0,#ffe3f0 30px,transparent 60px),
      radial-gradient(circle at 95% 45%,#fbd2e4 0,transparent 80px),
      radial-gradient(circle at 96% 60%,#e9f5c8 0,transparent 50px),
      linear-gradient(180deg,#f8d8e7,#f3dbe9)}
  .menu-card .sand{position:absolute;left:0;right:0;top:476px;bottom:0;background:linear-gradient(180deg,#cfa77a,#c59a6c 60%,#b98d61)}
  .menu-panel{position:absolute;left:28px;width:464px;top:0;height:476px;background:
      radial-gradient(circle at 22% 36%,rgba(200,110,210,.55) 0,transparent 70px),
      radial-gradient(circle at 75% 70%,rgba(175,90,200,.5) 0,transparent 90px),
      radial-gradient(circle at 60% 30%,rgba(160,80,180,.4) 0,transparent 60px),
      var(--panel)}
  .menu-panel.lower{top:476px;height:254px;background:linear-gradient(180deg,rgba(120,40,110,.92),rgba(125,50,100,.9))}

  .brand-tab{position:absolute;left:204px;top:0;width:148px;height:104px;background:var(--white);display:flex;flex-direction:column;align-items:center;justify-content:center;gap:6px}
  .brand-tab .dot{width:34px;height:34px;border-radius:50%;background:var(--ink)}
  .brand-name{font-family:"Oswald",sans-serif;font-weight:500;color:var(--ink);font-size:15px;letter-spacing:1px;text-align:center;line-height:1.05;text-transform:uppercase}

  .section-bar{position:absolute;left:0;width:568px;height:28px;background:linear-gradient(90deg,var(--teal) 0 28px,#4b60a8 28px,#6c3f9c 60%,rgba(140,60,160,.85) 464px,rgba(210,170,210,.5) 492px,transparent 568px)}
  .section-title{position:absolute;left:40px;top:3px;font-family:"Orbitron",sans-serif;font-weight:500;color:var(--heading);font-size:14px;letter-spacing:1.5px;text-transform:uppercase}
  .section-title b{font-size:19px;font-weight:500}

  .drink{position:absolute;left:38px;width:520px}
  .drink-name{color:var(--white);font-size:16px;font-weight:400;line-height:21px}
  .drink-line{display:flex;align-items:baseline;height:21px}
  .drink-notes{font-family:"Crimson Text",serif;font-style:italic;color:var(--white);font-size:15px;white-space:nowrap}
  .drink-notes.long{font-size:14px}
  .leader{flex:1;border-bottom:1.5px dotted rgba(255,255,255,.85);margin:0 4px 4px}
  .drink-price{width:62px;color:var(--price);font-size:17px;font-weight:500;padding-left:4px}

  /* ---------- Back: contact side ---------- */
  .cover-card{position:absolute;left:660px;top:150px;width:500px;height:650px;overflow:hidden;box-shadow:0 8px 24px rgba(0,0,0,.35)}
  .cover-photo{position:absolute;inset:0;background:
      radial-gradient(circle at 20% 20%,#d6f0c8 0,transparent 90px),
      radial-gradient(circle at 50% 15%,#ff9a8a 0,transparent 80px),
      radial-gradient(circle at 80% 25%,#ff4fa8 0,transparent 90px),
      radial-gradient(circle at 30% 50%,#ff3f9c 0,transparent 100px),
      radial-gradient(circle at 70% 55%,#ffb08a 0,transparent 110px),
      radial-gradient(circle at 15% 80%,#e4f4d0 0,transparent 90px),
      radial-gradient(circle at 90% 85%,#ff8a9e 0,transparent 100px),
      linear-gradient(135deg,#ffc3a6,#ff6fae 55%,#f2e6d0)}
  .cover-tab{position:absolute;left:160px;top:406px;width:180px;height:150px;background:linear-gradient(180deg,#ffffff,#f2e4f2);border-radius:26px 26px 0 0;display:flex;flex-direction:column;align-items:center;justify-content:center;gap:8px}
  .cover-tab .dot{width:50px;height:50px;border-radius:50%;background:var(--ink)}
  .cover-tab .brand-name{font-size:20px}
  .contact-band{position:absolute;left:0;right:0;top:556px;height:94px;background:linear-gradient(90deg,#f8f0f7 0,#e8c6e6 40%,#c468c4 100%);display:flex;flex-direction:column;align-items:center;justify-content:center;gap:2px;color:var(--ink)}
  .contact-web{font-size:16px;font-weight:500;line-height:20px}
  .contact-phone{font-family:"Michroma",sans-serif;font-size:22px;letter-spacing:1px;line-height:28px}
  .contact-address{font-size:14px;font-weight:500;line-height:18px}
</style>
</head>
<body>

<section class="menu-card" aria-label="Cocktail menu">
  <div class="side-glow" role="img" aria-label="Soft pink bokeh light background"></div>
  <div class="sand" role="img" aria-label="Photo of water droplets on a tan surface"></div>
  <div class="menu-panel" role="img" aria-label="Purple bokeh light background"></div>
  <div class="menu-panel lower"></div>

  <div class="brand-tab">
    <span class="dot"></span>
    <span class="brand-name">Hollowmere<br>Restaurant</span>
  </div>

  <div class="drink" style="top:106px">
    <div class="drink-name">Southern Manhattan</div>
    <div class="drink-line"><span class="drink-notes">Smooth Marlow Reserve Whiskey, Sweet Vermouth, Bourbon Cherries</span><span class="leader"></span><span class="drink-price">$12</span></div>
  </div>

  <div class="section-bar" style="top:158px"><h2 class="section-title"><b>M</b>artinis</h2></div>

  <div class="drink" style="top:190px">
    <div class="drink-name">The Old Banker</div>
    <div class="drink-line"><span class="drink-notes">Iced Cold Tobin's Handmade Vodka, Blue Cheese Olives</span><span class="leader"></span><span class="drink-price">$12</span></div>
  </div>
  <div class="drink" style="top:237px">
    <div class="drink-name">French Kiss Martini</div>
    <div class="drink-line"><span class="drink-notes">Stova Raspberry, Chantelle, Pineapple</span><span class="leader"></span><span class="drink-price">$10</span></div>
  </div>
  <div class="drink" style="top:284px">
    <div class="drink-name">Honey Apple Nip Martini</div>
    <div class="drink-line"><span class="drink-notes long">Honey Jack Darrow, Gander Vodka, Cider, Fall Spices and touch of Honey</span><span class="leader"></span><span class="drink-price">$11</span></div>
  </div>
  <div class="drink" style="top:331px">
    <div class="drink-name">Italiano Lemon Drop</div>
    <div class="drink-line"><span class="drink-notes">Stova Citrus Vodka, Lemoncello, Crystallized Rim, Lemon Twist</span><span class="leader"></span><span class="drink-price">$11</span></div>
  </div>
  <div class="drink" style="top:378px">
    <div class="drink-name">Cheng Jiang Martini</div>
    <div class="drink-line"><span class="drink-notes">Bacara O, Canto Ginger, Tavira, OJ</span><span class="leader"></span><span class="drink-price">$11</span></div>
  </div>
  <div class="drink" style="top:425px">
    <div class="drink-name">Perfect Pear</div>
    <div class="drink-line"><span class="drink-notes">Absolvo Pear Vodka, St. Gervais, Peach Schnapps, Apple Juice</span><span class="leader"></span><span class="drink-price">$10</span></div>
  </div>

  <div class="section-bar" style="top:476px"><h2 class="section-title"><b>C</b>ocktails</h2></div>

  <div class="drink" style="top:510px">
    <div class="drink-name">The Tipsy Judge</div>
    <div class="drink-line"><span class="drink-notes">Prosecco, St. Gervais, Gin, and Japanese Yuzu, and a Strawberry</span><span class="leader"></span><span class="drink-price">$12</span></div>
  </div>
  <div class="drink" style="top:557px">
    <div class="drink-name">Tart Love</div>
    <div class="drink-line"><span class="drink-notes">Bombard Gin, Campello, St. Gervais, Pineapple</span><span class="leader"></span><span class="drink-price">$10</span></div>
  </div>
  <div class="drink" style="top:604px">
    <div class="drink-name">I Love Lolo</div>
    <div class="drink-line"><span class="drink-notes">Stova Vanilla, Chantelle, Pineapple Juice, Champagne</span><span class="leader"></span><span class="drink-price">$10</span></div>
  </div>
  <div class="drink" style="top:651px">
    <div class="drink-name">Brazilian Fresh</div>
    <div class="drink-line"><span class="drink-notes">12 Reed Rum, Fresh Lime, and Grapefruit</span><span class="leader"></span><span class="drink-price">$12</span></div>
  </div>
</section>

<section class="cover-card" aria-label="Menu back cover">
  <div class="cover-photo" role="img" aria-label="Close-up photo of colourful pink, orange and mint drinking straws"></div>
  <div class="cover-tab">
    <span class="dot"></span>
    <span class="brand-name">Hollowmere<br>Restaurant</span>
  </div>
  <div class="contact-band">
    <div class="contact-web">www.hollowmererestaurant.com</div>
    <div class="contact-phone">703-555-0148</div>
    <div class="contact-address">24 Harrow Lane, Fairmont Virginia 20199</div>
  </div>
</section>

</body>
</html>
```